Webdesign für Beratung und Service im Bereich Heizungs- und Kühltechnologie
Zielgruppe
Wir sind ein modernes Dienstleistungsunternehmen, dass im Bereich Beratung und Service für Heizungs- und Kühltechnologie tätig ist. Wir suchen ein modernes Webdesign, das sich überwiegend an Geschäfts- / Gewerbekunden richten soll.
Aufgabenstellung
Wir möchten die in unserem Logo verwendete Farben auf der Webseite wiederfinden, Bilder werden mitgeliefert, müssen aber keine Verwendung finden. Wichtig ist das Hervorheben als Kundendienstvertretung des Premium-Herstellers BRK mit deren Logo und direktem Link auf deren Webseite. Gerne würden wir einen modernen Ansatz sehen, abweichend von den Standard-Seiten anderer Wartungsfirmen in unserer Branche.

```html
<!DOCTYPE html>
<html lang="de">
<head>
<meta charset="utf-8">
<title>Thermova GmbH – Heizungs- und Kühltechnologie</title>
<link rel="stylesheet" href="https://fonts.googleapis.com/css2?family=Fira+Sans:wght@300;400;500;600;700&display=swap">
<style>
:root{
  --navy:#0b355c;
  --blue:#0f4a78;
  --blue-light:#1d6795;
  --red:#c23c38;
  --red-dark:#9b2727;
  --grey:#f5f5f5;
  --text:#2a2a2a;
  --white:#ffffff;
}
*{box-sizing:border-box;margin:0;padding:0}
html,body{width:1200px;height:3061px;overflow:hidden}
body{position:relative;background:var(--white);font-family:"Fira Sans",Arial,sans-serif;color:var(--text)}
.abs{position:absolute}
svg.abs{display:block}

/* header */
.brand{left:222px;top:12px;display:flex;align-items:center;gap:10px}
.brand-dot{width:22px;height:22px;border-radius:50%;background:var(--red)}
.brand-name{font-size:26px;font-weight:600;color:var(--navy)}
.brand-claim{left:222px;top:56px;font-size:8px;font-weight:600;color:var(--navy)}
.nav{left:725px;top:30px;display:flex;gap:14px;font-size:10px;color:var(--white);letter-spacing:.3px}
.nav span.sep{opacity:.8}

.hero-intro{left:222px;top:155px;width:340px}
.hero-kicker{font-size:12px;font-weight:300;color:var(--red)}
.hero-title{margin-top:4px;font-size:22px;line-height:25px;font-weight:600;color:var(--navy)}
.hero-text{margin-top:40px;font-size:11px;line-height:16px;font-weight:400}

/* contact cards */
.avatar{width:94px;height:94px;border-radius:50%;border:2px solid var(--red)}
.avatar-agent{left:358px;top:489px;background:radial-gradient(circle at 50% 45%,#d9b9a3,#7b5240 70%)}
.avatar-desk{left:750px;top:489px;background:radial-gradient(circle at 50% 60%,#c7a788,#3f2a1f 70%)}
.contact-card{width:366px;height:86px;top:564px;border-radius:3px;background:linear-gradient(180deg,var(--blue),var(--navy));color:var(--white);text-align:center;font-size:12px;font-weight:600;padding-top:32px}
.contact-card svg{display:block;margin:0 auto 8px}
.card-left{left:222px}
.card-right{left:614px}
.card-left,.card-right{z-index:1}
.avatar{z-index:2}

.location-card{top:674px;width:366px;height:337px;border-radius:3px;background:linear-gradient(180deg,#27577c,#1b4a72 60%,#153f63);color:var(--white);text-align:center;font-size:10px;line-height:15px;padding-top:16px}
.location-card svg{display:block;margin:0 auto 6px}
.location-card strong{display:block;font-size:11px;font-weight:600;margin-bottom:2px}
.map{position:absolute;left:13px;top:120px;width:340px;height:190px;border:2px solid var(--red);background:linear-gradient(135deg,#b9d7a4,#d6e8c3 50%,#a8cd93)}

/* portfolio */
.portfolio-bg{left:0;top:1150px;width:1200px;height:1300px;background:var(--grey)}
.section-title{width:1200px;left:0;text-align:center;font-size:20px;font-weight:600;color:var(--navy)}
.photo-red{left:286px;top:1375px;width:177px;height:222px;border-radius:4px;background:linear-gradient(180deg,#c64a45,#9e2f2d)}
.photo-blue{left:241px;top:1301px;width:177px;height:223px;border-radius:4px;background:linear-gradient(180deg,#2a6a93,#19507c);box-shadow:0 4px 12px rgba(0,0,0,.2)}
.block-heading{font-size:14px;font-weight:400;color:var(--red-dark)}
.block-text p{font-size:9px;line-height:15px;margin-top:10px}
.who{left:489px;top:1338px;width:470px}
.offer{left:241px;top:1703px;width:470px}
.partner-row{left:241px;top:1822px;display:flex;align-items:center;gap:28px}
.partner-name{font-size:22px;font-weight:700;color:var(--red)}
.partner-link{font-size:10px;color:var(--navy);text-decoration:underline}
.product{left:770px;top:1655px;width:192px;height:246px;border-radius:4px;background:linear-gradient(180deg,#e6e8ea,#b7bcc0 60%,#8d9297)}

.service-box{left:222px;top:1966px;width:758px;height:341px;background:var(--white);border-bottom:3px solid var(--navy);box-shadow:0 2px 10px rgba(0,0,0,.08)}
.service-title{position:absolute;left:0;top:48px;width:100%;text-align:center;font-size:15px;font-weight:500;color:var(--red-dark)}
.service-item{position:absolute;width:240px;text-align:center;font-size:9px;font-weight:600;color:var(--navy)}
.service-brand{display:block;font-size:14px;font-weight:700;color:var(--blue);margin-bottom:16px;line-height:18px}
.service-item svg{display:block;margin:0 auto 10px}

/* emergency */
.emergency-bg{left:0;top:2480px;width:1200px;height:581px;background:var(--navy)}
.section-title.light{color:var(--white)}
.form-card{left:228px;top:2598px;width:746px;height:365px;background:var(--white);border-bottom:3px solid var(--red)}
.emergency-info{position:absolute;left:22px;top:22px;width:228px;font-size:9px;line-height:14px}
.emergency-info .intro{display:flex;gap:12px}
.emergency-info ul{list-style:none;margin-top:18px;font-weight:600}
.emergency-info li::before{content:"›";margin-right:10px;font-weight:400}
.emergency-info .hint{margin-top:14px}
.call-button{margin-top:12px;width:224px;height:48px;background:var(--navy);color:var(--white);font-size:11px;font-weight:600;display:flex;align-items:center;gap:28px;padding-left:20px;border-radius:2px}
.field{position:absolute;height:28px;border:1px solid #c9c9c9;font-size:9px;font-style:italic;color:#aaa;padding:7px 10px;font-weight:300}
.send{position:absolute;left:260px;top:280px;width:462px;height:29px;background:var(--navy);color:var(--white);font-size:8px;font-weight:700;text-align:center;line-height:29px;border-radius:2px}

.footer{left:234px;top:3020px;width:728px;display:flex;justify-content:space-between;font-size:8px;color:var(--white)}
.footer-links{display:flex;gap:8px}
.footer-links span{text-decoration:underline}
</style>
</head>
<body>

<!-- hero shape -->
<svg class="abs" style="left:0;top:0" width="1200" height="430" viewBox="0 0 1200 430">
  <defs>
    <linearGradient id="heroBlue" x1="0" y1="0" x2="1" y2="1">
      <stop offset="0" stop-color="#1d5f8e"/>
      <stop offset="1" stop-color="#0b355c"/>
    </linearGradient>
    <linearGradient id="heroRed" x1="0" y1="0" x2="1" y2="0">
      <stop offset="0" stop-color="#d0504a"/>
      <stop offset="1" stop-color="#9b2727"/>
    </linearGradient>
  </defs>
  <path d="M528,0 C570,110 560,230 660,320 C780,420 980,425 1200,390 L1200,0 Z" fill="url(#heroRed)"/>
  <path role="img" aria-label="Foto: Handschlag zweier Geschäftsleute" d="M575,0 C605,110 610,220 700,300 C810,395 990,400 1200,372 L1200,0 Z" fill="url(#heroBlue)"/>
</svg>

<div class="abs brand"><span class="brand-dot"></span><span class="brand-name">Thermova</span></div>
<div class="abs brand-claim">High Efficient Heating &amp; Cooling Services</div>
<nav class="abs nav"><span>START</span><span class="sep">•</span><span>PORTFOLIO</span><span class="sep">•</span><span>WARTUNG</span><span class="sep">•</span><span>NOTDIENST</span></nav>

<section class="abs hero-intro">
  <p class="hero-kicker">Willkommen bei der Thermova GmbH</p>
  <h1 class="hero-title">Ihr Spezialist für Beratung und Service im Bereich der Heizungs- und Kühltechnologie</h1>
  <p class="hero-text">Für uns sind Kundenzufriedenheit und Service-Qualität täglich gelebte Unternehmensphilosophie und keine Phrasen.</p>
</section>

<!-- contact -->
<div class="abs avatar avatar-agent" role="img" aria-label="Foto: Servicemitarbeiterin mit Headset"></div>
<div class="abs avatar avatar-desk" role="img" aria-label="Foto: Hände an einer Laptop-Tastatur"></div>
<div class="abs contact-card card-left">
  <svg width="13" height="13" viewBox="0 0 24 24"><path d="M6.6 10.8a15 15 0 0 0 6.6 6.6l2.2-2.2c.3-.3.7-.4 1-.2 1.1.4 2.3.6 3.6.6.6 0 1 .4 1 1V20c0 .6-.4 1-1 1A17 17 0 0 1 3 4c0-.6.4-1 1-1h3.5c.6 0 1 .4 1 1 0 1.3.2 2.5.6 3.6.1.3 0 .7-.2 1z" fill="#fff"/></svg>
  +49 (0) 8000 5550100 20
</div>
<div class="abs contact-card card-right">
  <svg width="14" height="12" viewBox="0 0 24 20"><rect x="1.5" y="1.5" width="21" height="17" rx="1.5" fill="none" stroke="#fff" stroke-width="2"/><path d="M2 3l10 8 10-8" fill="none" stroke="#fff" stroke-width="2"/></svg>
  info@thermova-service.de
</div>

<div class="abs location-card" style="left:222px">
  <svg width="12" height="16" viewBox="0 0 24 32"><path d="M12 1a10 10 0 0 0-10 10c0 8 10 20 10 20s10-12 10-20A10 10 0 0 0 12 1z" fill="none" stroke="#fff" stroke-width="3"/><circle cx="12" cy="11" r="3.5" fill="#fff"/></svg>
  <strong>Firmensitz:</strong>Thermova GmbH<br>Lindenhof 12<br>85600 Musterau – Lindenhof
  <div class="map" role="img" aria-label="Karte des Firmensitzes"></div>
</div>
<div class="abs location-card" style="left:614px">
  <svg width="12" height="16" viewBox="0 0 24 32"><path d="M12 1a10 10 0 0 0-10 10c0 8 10 20 10 20s10-12 10-20A10 10 0 0 0 12 1z" fill="none" stroke="#fff" stroke-width="3"/><circle cx="12" cy="11" r="3.5" fill="#fff"/></svg>
  <strong>Service Zentrale:</strong>Thermova GmbH<br>Amselweg 4<br>37400 Talheim
  <div class="map" role="img" aria-label="Karte der Service Zentrale"></div>
</div>

<!-- portfolio -->
<div class="abs portfolio-bg"></div>
<svg class="abs" style="left:0;top:1090px" width="1200" height="160" viewBox="0 0 1200 160">
  <defs>
    <linearGradient id="waveRed" x1="0" y1="0" x2="1" y2="0">
      <stop offset="0" stop-color="#d5534c"/>
      <stop offset="1" stop-color="#9b2727"/>
    </linearGradient>
  </defs>
  <path d="M0,0 H1200 V160 H0 Z" fill="#fff"/>
  <path d="M0,75 C350,10 800,30 1200,150 L1200,160 L0,160 Z" fill="#f5f5f5"/>
  <path d="M0,28 C350,-18 800,5 1200,100 L1200,152 C800,30 350,10 0,78 Z" fill="url(#waveRed)"/>
</svg>
<h2 class="abs section-title" style="top:1199px">Portfolio</h2>

<div class="abs photo-red" role="img" aria-label="Foto: rote Heizungsanlage"></div>
<div class="abs photo-blue" role="img" aria-label="Foto: Anlagentechnik auf einem Dach"></div>
<section class="abs who block-text">
  <h3 class="block-heading">Wer sind wir</h3>
  <p style="margin-top:18px">Wir sind ein modernes Beratungs- und Service-Unternehmen mit hochmotivierten Mitarbeitern, die seit Jahrzehnten in der Heizungs- und Klimabranche tätig sind.</p>
  <p>Unsere Mitarbeiter sind stets auf den neuesten Stand der Technik geschult.</p>
  <p>Verteilte Servicestationen machen es möglich, dass wir Ihnen deutschlandweit an 365 Tagen / 24 Stunden unsere Dienste anbieten können.</p>
  <p>Optimierte Einsatzplanung garantieren Ihnen schnelle Reaktionszeiten.</p>
  <p>Schlanke Prozessstrukturen sorgen für eine reibungslose Ersatzteilversorgung.</p>
  <p>Profitieren Sie von dem tiefgreifenden Know-How unsere Mitarbeiter, ihren langjährigen Erfahrungen und dem hohen Qualitätsanspruch unseres Unternehmens.</p>
</section>

<section class="abs offer block-text">
  <h3 class="block-heading">Was bieten wir an</h3>
  <p style="margin-top:18px">In unserem Fokus stehen Heizungs- und Kühltechnologie mit hoher Effizienz und Rückhaltigkeit.</p>
  <p>Als Kundendienstvertretung des Schweizer Premium-Herstellers BRK, übernehmen wir alle Kundendienstleistungen für Inbetriebnahmen, Gewährleistungs- Wartungs- und Servicearbeiten für deren Produktportfolio (u.a. Luft-Wasser oder Sole-Wasser Wärmepumpen, Splitgeräte und Serverraumkühlungen).</p>
</section>
<div class="abs partner-row"><span class="partner-name">BRK</span><span class="partner-link">BRK AG, Klima-Kälte-Wärme &gt;</span></div>
<div class="abs product" role="img" aria-label="Produktfoto: zwei Wärmepumpen-Geräte"></div>

<section class="abs service-box">
  <h3 class="service-title">Außerdem bieten wir Service und Wartungsarbeiten für folgende Produkte an:</h3>
  <div class="service-item" style="left:75px;top:106px"><span class="service-brand">Norvaklima</span>Klimaanlagen der Firma Norvaklima</div>
  <div class="service-item" style="left:442px;top:106px"><span class="service-brand">Calvento</span>Calvento-Wärmepumpen</div>
  <div class="service-item" style="left:14px;top:196px"><span class="service-brand" style="margin-bottom:8px">Hallbrand<br>Kessler<br>Ostwerk</span>Heizungswartungen und Austausch an Hallbrand, Kessler, Ostwerk etc.</div>
  <div class="service-item" style="left:259px;top:208px">
    <svg width="46" height="46" viewBox="0 0 46 46" fill="none" stroke="#0f4a78" stroke-width="1.6"><circle cx="23" cy="6" r="3.5"/><path d="M23 0v-1M17 6h-2M31 6h-2"/><rect x="4" y="18" width="38" height="20"/><path d="M4 28h38M16.7 18v20M29.3 18v20M23 38v6M15 44h16"/></svg>
    Solaranlagen
  </div>
  <div class="service-item" style="left:503px;top:216px"><span class="service-brand">Voltaria</span>BHKW der Firmen Enerkon und Voltaria</div>
</section>

<!-- emergency -->
<div class="abs emergency-bg"></div>
<svg class="abs" style="left:0;top:2350px" width="1200" height="140" viewBox="0 0 1200 140">
  <path d="M0,8 C260,40 520,135 820,135 C1000,135 1120,110 1200,90 L1200,140 L0,140 Z" fill="#0b355c"/>
</svg>
<h2 class="abs section-title light" style="top:2527px">Notdienst</h2>

<section class="abs form-card">
  <div class="emergency-info">
    <div class="intro">
      <svg width="26" height="26" viewBox="0 0 24 24" fill="none" stroke="#c23c38" stroke-width="1.6"><path d="M6 17V11a6 6 0 0 1 12 0v6l2 2H4z"/><path d="M10 21a2 2 0 0 0 4 0"/></svg>
      <p>Unser Notdienst steht Ihnen für folgende Leistungen zur Verfügung: Identifizieren und Beheben von Betriebs-Störungen an:</p>
    </div>
    <ul><li>Wärmepumpen</li><li>Heizungsanlagen</li><li>Klimaanlagen</li><li>Solaranlagen</li></ul>
    <p class="hint">Sie erreichen uns deutschlandweit unter der Tel.-Nr:</p>
    <div class="call-button">
      <svg width="13" height="13" viewBox="0 0 24 24"><path d="M6.6 10.8a15 15 0 0 0 6.6 6.6l2.2-2.2c.3-.3.7-.4 1-.2 1.1.4 2.3.6 3.6.6.6 0 1 .4 1 1V20c0 .6-.4 1-1 1A17 17 0 0 1 3 4c0-.6.4-1 1-1h3.5c.6 0 1 .4 1 1 0 1.3.2 2.5.6 3.6.1.3 0 .7-.2 1z" fill="#fff"/></svg>
      +49 (0) 8000 5550100 20
    </div>
  </div>
  <div class="field" style="left:260px;top:22px;width:222px">Name*</div>
  <div class="field" style="left:500px;top:22px;width:222px">E-Mail*</div>
  <div class="field" style="left:260px;top:58px;width:222px">Telefonnummer</div>
  <div class="field" style="left:500px;top:58px;width:222px">Betreff*</div>
  <div class="field" style="left:260px;top:94px;width:462px;height:171px">Nachricht*</div>
  <div class="send">SENDEN</div>
</section>

<footer class="abs footer">
  <span>© 2019 Thermova – Intelligent Heating &amp; Cooling. Alle Rechte vorbehalten.</span>
  <span class="footer-links"><span>AGB</span><span>DATENSCHUTZERKLÄRUNG</span><span>IMPRESSUM</span></span>
</footer>

</body>
</html>
```